Need a business card design for a new business

The business is going to be called "The Maple Lectern" - it is an online training company that provides Instructor Lead training to students at any destination in the world
The reference to cloud is the internet and classroom reference will be a computer at the students and instructors end

We will need a Web site and stationary and advertising material developed over time but for now require the business cards only

So if we are happy with the business card then we will use the same designers for the other requirments of the business as it evolves

Industry/Entity Type

Advertising

```html
<!DOCTYPE html>
<html lang="en">
<head>
<meta charset="utf-8">
<title>The Maple Lectern — Business Card</title>
<link rel="stylesheet" href="https://fonts.googleapis.com/css2?family=Almendra:wght@400;700&family=Arvo:wght@700&display=swap">
<style>
  :root {
    --backdrop: #b8ab93;
    --card: #f4f4f6;
    --ink: #1b1b1b;
    --mark-blue: #2f3b9c;
    --name-grey: #8a8a8a;
    --rule-grey: #9a9a9a;
  }
  * { box-sizing: border-box; margin: 0; padding: 0; }
  html, body { width: 1200px; height: 862px; overflow: hidden; }
  body { background: var(--backdrop); position: relative; }

  .card {
    position: absolute;
    width: 632px;
    height: 358px;
    background: var(--card);
    box-shadow: 0 3px 10px rgba(0,0,0,0.25);
  }
  .card--front { left: 40px; top: 60px; }
  .card--back  { left: 537px; top: 455px; }

  .brand {
    position: absolute;
    display: flex;
    align-items: center;
    font-family: "Almendra", serif;
    font-weight: 700;
    color: var(--ink);
    white-space: nowrap;
  }
  .brand__dot {
    border-radius: 50%;
    background: var(--mark-blue);
    flex: none;
  }
  .card--front .brand { left: 70px; top: 145px; font-size: 50px; gap: 22px; }
  .card--front .brand__dot { width: 56px; height: 56px; }
  .card--back .brand { left: 16px; top: 52px; font-size: 27px; gap: 12px; }
  .card--back .brand__dot { width: 30px; height: 30px; }

  .holder {
    position: absolute;
    right: 28px;
    top: 12px;
    text-align: right;
    color: var(--name-grey);
  }
  .holder__name { font-family: "Arvo", serif; font-weight: 700; font-size: 33px; line-height: 1.1; }
  .holder__role { font-family: "Almendra", serif; font-size: 25px; line-height: 1.1; }

  .contact-rule {
    position: absolute;
    left: 213px;
    top: 153px;
    width: 4px;
    height: 200px;
    background: var(--rule-grey);
  }
  .contact {
    position: absolute;
    left: 237px;
    top: 158px;
    list-style: none;
    font-family: "Almendra", serif;
    font-size: 21px;
    line-height: 31px;
    color: var(--ink);
  }
</style>
</head>
<body>
  <section class="card card--front" aria-label="Card front">
    <div class="brand"><span class="brand__dot"></span>The Maple Lectern</div>
  </section>

  <section class="card card--back" aria-label="Card back">
    <div class="brand"><span class="brand__dot"></span>The Maple Lectern</div>
    <div class="holder">
      <div class="holder__name">Dana Whitlow</div>
      <div class="holder__role">Manger</div>
    </div>
    <div class="contact-rule"></div>
    <ul class="contact">
      <li>Phone: 432-555-0187</li>
      <li>Fax: 341-555-0142</li>
      <li>Email: dana@maplelectern.com</li>
      <li>1172 Birchwood Ct.</li>
      <li>Marlow, IA 50012</li>
      <li>www.TheMapleLectern.com</li>
    </ul>
  </section>
</body>
</html>
```